Commercial Construction Company

We need a business card design based on our current logo. We are a commercial general contractor based in Southern California that specializes in bank remodels. We would like to see designs that incorporate dark blue. The final design should portray an image of professionalism and quality.

If possible, I would like to add metallic foil to the design. Thank you

```html
<!DOCTYPE html>
<html lang="en">
<head>
<meta charset="utf-8">
<title>Halden Commercial Builders — Business Card</title>
<link href="https://fonts.googleapis.com/css2?family=Open+Sans:wght@400;700&display=swap" rel="stylesheet">
<style>
  :root {
    --navy: #124a80;
    --silver: #d9dadc;
    --ink: #555759;
    --paper: #ffffff;
    --backdrop: #9c9c9c;
  }
  * { box-sizing: border-box; margin: 0; padding: 0; }
  html, body { width: 1049px; height: 1200px; overflow: hidden; }
  body {
    background: var(--backdrop);
    font-family: "Open Sans", Arial, sans-serif;
    position: relative;
  }
  .card {
    position: absolute;
    left: 164px;
    width: 722px;
    height: 413px;
    border-radius: 26px;
  }
  .card--front { top: 140px; background: var(--navy); }
  .card--back { top: 646px; background: var(--paper); }

  .brand {
    position: absolute;
    display: flex;
    align-items: center;
    gap: 14px;
    font-weight: 700;
  }
  .brand__dot {
    width: 34px; height: 34px;
    border-radius: 50%;
    flex: none;
  }
  .brand__name { line-height: 1.05; letter-spacing: 1px; }
  .brand__name span { display: block; }
  .brand__main { font-size: 44px; }
  .brand__sub { font-size: 13px; letter-spacing: 3px; }

  .card--front .brand {
    left: 50%; top: 50%;
    transform: translate(-50%, -50%);
    color: var(--silver);
  }
  .card--front .brand__dot { background: var(--silver); }

  .card--back .brand {
    left: 106px; top: 164px;
    color: var(--navy);
  }
  .card--back .brand__main { font-size: 40px; }
  .card--back .brand__sub { font-size: 12px; }
  .card--back .brand__dot { background: var(--navy); }

  .divider {
    position: absolute;
    left: 389px; top: 114px;
    width: 2px; height: 187px;
    background: var(--navy);
  }
  .contact-block {
    position: absolute;
    left: 414px; top: 104px;
  }
  .person__name {
    color: var(--navy);
    font-weight: 700;
    font-size: 28px;
    line-height: 1.2;
  }
  .person__role {
    color: var(--ink);
    font-size: 19px;
    line-height: 1.2;
    margin-bottom: 27px;
  }
  .contact-list { list-style: none; }
  .contact-list li {
    display: flex;
    align-items: center;
    gap: 7px;
    color: var(--ink);
    font-size: 20px;
    line-height: 27.5px;
  }
  .icon { width: 17px; height: 17px; fill: var(--navy); flex: none; }
  .address {
    position: absolute;
    left: 128px; top: 358px;
    display: flex; align-items: center; gap: 7px;
    color: var(--ink);
    font-size: 20px;
  }
</style>
</head>
<body>
  <section class="card card--front">
    <div class="brand">
      <div class="brand__dot"></div>
      <div class="brand__name">
        <span class="brand__main">HALDEN</span>
        <span class="brand__sub">COMMERCIAL BUILDERS</span>
      </div>
    </div>
  </section>

  <section class="card card--back">
    <div class="brand">
      <div class="brand__dot"></div>
      <div class="brand__name">
        <span class="brand__main">HALDEN</span>
        <span class="brand__sub">COMMERCIAL BUILDERS</span>
      </div>
    </div>

    <div class="divider"></div>

    <div class="contact-block">
      <h1 class="person__name">DANIEL REEVE</h1>
      <p class="person__role">President</p>
      <ul class="contact-list">
        <li>
          <svg class="icon" viewBox="0 0 24 24"><path d="M6.6 10.8a15.1 15.1 0 0 0 6.6 6.6l2.2-2.2a1 1 0 0 1 1-.25 11.4 11.4 0 0 0 3.6.57 1 1 0 0 1 1 1V20a1 1 0 0 1-1 1A17 17 0 0 1 3 4a1 1 0 0 1 1-1h3.5a1 1 0 0 1 1 1c0 1.25.2 2.45.57 3.57a1 1 0 0 1-.25 1z"/></svg>
          949-555-0187
        </li>
        <li>
          <svg class="icon" viewBox="0 0 24 24"><path d="M7 1h10a2 2 0 0 1 2 2v18a2 2 0 0 1-2 2H7a2 2 0 0 1-2-2V3a2 2 0 0 1 2-2zm0 3v14h10V4zm5 15.5a1.2 1.2 0 1 0 0 2.4 1.2 1.2 0 0 0 0-2.4z"/></svg>
          949-555-0187
        </li>
        <li>
          <svg class="icon" viewBox="0 0 24 24"><path d="M2 5h20v2l-10 6L2 7zm0 4.3 10 6 10-6V19H2z"/></svg>
          dan@haldenbuild.com
        </li>
        <li>
          <svg class="icon" viewBox="0 0 24 24"><path d="M12 2a10 10 0 1 0 0 20 10 10 0 0 0 0-20zm0 2c1 0 2.2 2 2.7 5H9.3C9.8 6 11 4 12 4zM4.3 10h3a20 20 0 0 0 0 4h-3a8 8 0 0 1 0-4zm5 0h5.4a18 18 0 0 1 0 4H9.3a18 18 0 0 1 0-4zm7.4 0h3a8 8 0 0 1 0 4h-3a20 20 0 0 0 0-4zM9.3 15h5.4c-.5 3-1.7 5-2.7 5s-2.2-2-2.7-5z"/></svg>
          www.haldenbuild.com
        </li>
      </ul>
    </div>

    <p class="address">
      <svg class="icon" viewBox="0 0 24 24"><path d="M12 1a8 8 0 0 0-8 8c0 6 8 14 8 14s8-8 8-14a8 8 0 0 0-8-8zm0 11a3 3 0 1 1 0-6 3 3 0 0 1 0 6z"/></svg>
      3150 Marina Crest Drive, Laguna Bay CA 92651
    </p>
  </section>
</body>
</html>
```